Tallow Creek Wines range of wine labels

Would like a sophisticated distinguished design for our wine label range for following varieties

2020 Shiraz
2021 Sauvignon Blanc
2021 Chardonnay
2021 Pinot Grigio
2020 Cabernet Sauvignon

Take artistic licence and present how the range will work together.

Preference is for wrap label - 180 mm wide to fit a standard Claret bottle

Of the width you have 90 mm wide of design that can be seen when bottle front on. Images can carry past this but won't be seen when looking straight on.

essentials to include on label back or front are
Vintage (eg 2020)
Varietal (eg Shiraz)
Region (all our South Australia)
description (allow for approximately 50 - 80 words)
Wine of Australia
% Alc/Vol 750Mls
number of standard drinks
address
Contains Sulphates (220)

Target Market(s)

Over 50s male and female

Font styles to use
Decorative

Requirements
Must have
• Open to designers take on project
Nice to have
• Foil or other considerations for definition

```html
<!DOCTYPE html>
<html lang="en">
<head>
<meta charset="utf-8">
<title>Tallow Creek Wines – 2021 Chardonnay Label</title>
<link rel="stylesheet" href="https://fonts.googleapis.com/css2?family=Montserrat:wght@400;500;700&family=Great+Vibes&display=swap">
<style>
  :root {
    --backdrop: #e9eaea;
    --label-paper: #ffffff;
    --label-edge: #d9dcdc;
    --teal-deep: #17888c;
    --teal-bright: #3fc0c3;
    --teal-pale: #a9e1e2;
    --ink: #2e6a70;
  }
  * { margin: 0; padding: 0; box-sizing: border-box; }
  html, body {
    width: 835px;
    height: 1200px;
    overflow: hidden;
    background: var(--backdrop);
  }
  .wine-label {
    position: absolute;
    left: 117px;
    top: 75px;
    width: 600px;
    height: 1050px;
    background: var(--label-paper);
    border: 1px solid var(--label-edge);
    box-shadow: 0 6px 24px rgba(0, 0, 0, 0.08);
    font-family: "Montserrat", sans-serif;
    color: var(--ink);
  }
  .seahorse-art {
    position: absolute;
    left: 40px;
    top: 300px;
    width: 190px;
    height: 700px;
    border-radius: 95px 95px 70px 70px;
    background: linear-gradient(165deg, var(--teal-bright) 0%, var(--teal-deep) 55%, var(--teal-pale) 100%);
  }
  .brand {
    position: absolute;
    left: 262px;
    top: 300px;
    width: 300px;
    text-align: left;
  }
  .brand-name {
    font-weight: 700;
    color: var(--teal-deep);
    font-size: 50px;
    line-height: 1.02;
    letter-spacing: 0.08em;
    text-transform: uppercase;
  }
  .brand-sub {
    margin-top: 10px;
    font-size: 17px;
    font-weight: 500;
    letter-spacing: 0.6em;
    color: var(--teal-deep);
    text-transform: uppercase;
  }
  .vintage {
    position: absolute;
    left: 230px;
    top: 560px;
    width: 340px;
    text-align: center;
    font-size: 40px;
    font-weight: 400;
    letter-spacing: 0.45em;
    padding-left: 0.45em;
  }
  .varietal {
    position: absolute;
    left: 220px;
    top: 625px;
    width: 360px;
    text-align: center;
    font-family: "Great Vibes", cursive;
    font-size: 74px;
    line-height: 1.1;
    color: var(--teal-deep);
  }
  .details {
    position: absolute;
    left: 240px;
    top: 800px;
    width: 330px;
    list-style: none;
    text-align: center;
    font-size: 15px;
    font-weight: 500;
    letter-spacing: 0.16em;
    line-height: 1.75;
    text-transform: uppercase;
  }
</style>
</head>
<body>
  <main class="wine-label">
    <div class="seahorse-art" role="img" aria-label="Teal seahorse illustration running down the left side of the label"></div>
    <header class="brand">
      <h1 class="brand-name">Tallow<br>Creek</h1>
      <p class="brand-sub">Wines</p>
    </header>
    <p class="vintage">2021</p>
    <p class="varietal">Chardonnay</p>
    <ul class="details">
      <li>South Australia</li>
      <li>Wine of Australia</li>
      <li>13.5% Alc/Vol 750mls</li>
    </ul>
  </main>
</body>
</html>
```